Letterhead and Envelope Design for Investment Company

We need a letterhead and envelope design.
We are a family owned investment company doing direct investments into other family owned businesses.
I have attached all our current marketing material including our logo for reference.

Our under construction website can be found here:
https://rob-darke-qv7m.pagevorlo.com/
password: Copperfen

Target Market(s)

Bankers, business owners, financial partners

Industry/Entity Type

Investment

Colors

Designer to choose colors to be used in the design.

Requirements
Must have
• Logo, and company information

```html
<!DOCTYPE html>
<html lang="en">
<head>
<meta charset="utf-8">
<title>Copperfen Holdings Stationery</title>
<link rel="stylesheet" href="https://fonts.googleapis.com/css2?family=Open+Sans:wght@400;600;700&display=swap">
<style>
  :root {
    --board: #a97c52;
    --ink: #1a1a1a;
    --paper: #ffffff;
    --gold: #d4a92a;
    --gold-deep: #c2961c;
    --text-dark: #333333;
    --text-light: #d8d8d8;
    --shadow: 2px 3px 6px rgba(0,0,0,0.35);
  }
  * { box-sizing: border-box; margin: 0; padding: 0; }
  html, body { width: 1200px; height: 740px; overflow: hidden; }
  body {
    background: var(--board);
    font-family: "Open Sans", sans-serif;
    position: relative;
  }
  .piece { position: absolute; box-shadow: var(--shadow); }

  .wordmark {
    font-family: "Open Sans", sans-serif;
    font-weight: 600;
    text-transform: uppercase;
    letter-spacing: 0.06em;
    white-space: nowrap;
    display: flex;
    align-items: center;
    gap: 0.5em;
  }
  .wordmark .dot { display: inline-block; border-radius: 50%; background: currentColor; }
  .on-dark { color: var(--paper); }
  .on-light { color: var(--text-dark); }

  /* Letterhead */
  .letterhead { left: 56px; top: 56px; width: 486px; height: 628px; background: var(--paper); }
  .letterhead-header { position: absolute; left: 0; top: 0; width: 486px; height: 140px; }
  .letterhead .letterhead-header-mark { position: absolute; left: 0; right: 0; top: 82px; justify-content: center; font-size: 13px; }
  .letterhead .letterhead-header-mark .dot { width: 7px; height: 7px; background: var(--gold); }
  .letterhead-footer {
    position: absolute; left: 24px; right: 18px; top: 572px; height: 40px;
    border-bottom: 1px solid #cfcfcf; font-size: 7.5px; color: var(--text-dark);
  }
  .letterhead-footer .contact { position: absolute; left: 0; top: 0; line-height: 12px; }
  .letterhead-footer .footer-mark {
    position: absolute; left: 50%; top: 26px; transform: translateX(-50%);
    font-size: 7px; letter-spacing: 0.04em; gap: 4px;
  }
  .letterhead-footer .footer-mark .dot { width: 4px; height: 4px; background: var(--gold); }
  .letterhead-footer .address { position: absolute; right: 0; top: 14px; text-align: right; line-height: 11px; }

  .contact-row { display: flex; align-items: center; gap: 4px; }
  .contact-row svg { flex: none; }

  /* Business cards */
  .card { width: 214px; height: 128px; }
  .card-front { left: 642px; top: 113px; background: var(--ink); }
  .card-front .wordmark { position: absolute; left: 0; right: 0; top: 67px; justify-content: center; font-size: 8.5px; gap: 4px; }
  .card-front .wordmark .dot { width: 5px; height: 5px; background: var(--gold); }
  .card-front .web { position: absolute; left: 0; right: 0; top: 97px; text-align: center; font-size: 6px; color: var(--text-light); }

  .card-back { left: 873px; top: 116px; width: 224px; background: var(--paper); }
  .card-back .wordmark { position: absolute; left: 10px; top: 69px; font-size: 6.5px; gap: 3px; letter-spacing: 0.03em; }
  .card-back .wordmark .dot { width: 4px; height: 4px; background: var(--gold); }
  .card-back .divider { position: absolute; left: 112px; top: 34px; width: 1px; height: 60px; background: #cccccc; }
  .card-back .details { position: absolute; left: 120px; top: 34px; font-size: 5.2px; line-height: 7.8px; color: var(--text-dark); }
  .card-back .name { font-size: 8px; font-weight: 700; color: var(--gold-deep); line-height: 9px; }
  .card-back .title { font-size: 5.5px; font-weight: 600; margin-bottom: 3px; }

  /* Envelope */
  .envelope-flap { left: 586px; top: 289px; width: 555px; height: 64px; box-shadow: none; filter: drop-shadow(2px 3px 3px rgba(0,0,0,0.35)); }
  .envelope-flap svg { position: absolute; inset: 0; }
  .envelope-flap .wordmark { position: absolute; left: 0; right: 0; top: 22px; justify-content: center; font-size: 7.5px; transform: rotate(180deg); gap: 4px; }
  .envelope-flap .wordmark .dot { width: 4px; height: 4px; background: var(--gold); }

  .envelope { left: 587px; top: 394px; width: 555px; height: 250px; background: var(--ink); }
  .envelope .wordmark { position: absolute; left: 29px; top: 72px; font-size: 13px; }
  .envelope .wordmark .dot { width: 7px; height: 7px; background: var(--gold); }
  .envelope .rule { position: absolute; left: 29px; top: 94px; width: 185px; height: 1px; background: var(--gold); }
  .envelope .contact { position: absolute; left: 29px; top: 200px; font-size: 7.5px; line-height: 12px; color: var(--text-light); }
  .envelope .contact .web { color: var(--gold); font-weight: 600; letter-spacing: 0.05em; }
  .envelope .address { position: absolute; left: 181px; top: 213px; font-size: 7.5px; line-height: 11px; color: var(--text-light); }
</style>
</head>
<body>

<svg width="0" height="0" style="position:absolute">
  <defs>
    <symbol id="icon-phone" viewBox="0 0 10 10"><circle cx="5" cy="5" r="4.4" fill="none" stroke="#d4a92a" stroke-width="1"/><path d="M3.4 2.8 Q3 5.8 6.6 7.2" fill="none" stroke="#d4a92a" stroke-width="1.3" stroke-linecap="round"/></symbol>
    <symbol id="icon-mail" viewBox="0 0 10 10"><rect x="1" y="2.5" width="8" height="5.5" fill="#d4a92a"/><path d="M1 2.5 L5 5.6 L9 2.5" fill="none" stroke="#fff" stroke-width="0.8"/></symbol>
    <symbol id="icon-web" viewBox="0 0 10 10"><circle cx="5" cy="5" r="4.2" fill="none" stroke="#d4a92a" stroke-width="1"/><path d="M1 5 H9 M5 1 Q2.5 5 5 9 M5 1 Q7.5 5 5 9" fill="none" stroke="#d4a92a" stroke-width="0.7"/></symbol>
  </defs>
</svg>

<!-- Letterhead -->
<section class="piece letterhead">
  <svg class="letterhead-header" viewBox="0 0 486 140" aria-hidden="true">
    <path d="M0 84 Q243 182 486 84 L486 92 Q243 190 0 92 Z" fill="var(--gold)"/>
    <path d="M0 0 H486 V78 Q243 162 0 78 Z" fill="var(--ink)"/>
  </svg>
  <div class="wordmark on-dark letterhead-header-mark"><span class="dot"></span>Copperfen Holdings Inc</div>

  <div class="letterhead-footer">
    <div class="contact">
      <div class="contact-row"><svg width="7" height="7"><use href="#icon-phone"/></svg>555 014 0426</div>
      <div class="contact-row"><svg width="7" height="7"><use href="#icon-mail"/></svg>rob.darke@copperfenholdings.com</div>
      <div class="contact-row"><svg width="7" height="7"><use href="#icon-web"/></svg>www.copperfenholdings.com</div>
    </div>
    <div class="wordmark on-light footer-mark"><span class="dot"></span>Copperfen Holdings Inc</div>
    <div class="address">48 Harlow Ave, Suite 210<br>Fenwick, IA 50010</div>
  </div>
</section>

<!-- Business card front -->
<section class="piece card card-front">
  <div class="wordmark on-dark"><span class="dot"></span>Copperfen Holdings Inc</div>
  <div class="web">www.copperfenholdings.com</div>
</section>

<!-- Business card back -->
<section class="piece card card-back">
  <div class="wordmark on-light"><span class="dot"></span>Copperfen Holdings</div>
  <div class="divider"></div>
  <div class="details">
    <div class="name">Rob Darke</div>
    <div class="title">Vice President</div>
    <div>48 Harlow Ave, Suite 210</div>
    <div>Fenwick, IA 50010</div>
    <div class="contact-row"><svg width="5" height="5"><use href="#icon-phone"/></svg>555 014 0426</div>
    <div class="contact-row"><svg width="5" height="5"><use href="#icon-mail"/></svg>rob.darke@copperfenholdings.com</div>
    <div class="contact-row"><svg width="5" height="5"><use href="#icon-web"/></svg>www.copperfenholdings.com</div>
  </div>
</section>

<!-- Envelope flap -->
<section class="piece envelope-flap">
  <svg viewBox="0 0 555 64" width="555" height="64" aria-hidden="true">
    <path d="M0 0 H555 L522 46 Q510 63 488 63 H68 Q46 63 34 46 Z" fill="var(--paper)"/>
  </svg>
  <div class="wordmark on-light"><span class="dot"></span>Copperfen Holdings Inc</div>
</section>

<!-- Envelope -->
<section class="piece envelope">
  <div class="wordmark on-dark"><span class="dot"></span>Copperfen Holdings Inc</div>
  <div class="rule"></div>
  <div class="contact">
    <div class="contact-row"><svg width="7" height="7"><use href="#icon-phone"/></svg>555 014 0426</div>
    <div class="contact-row"><svg width="7" height="7"><use href="#icon-mail"/></svg>rob.darke@copperfenholdings.com</div>
    <div class="contact-row web"><svg width="7" height="7"><use href="#icon-web"/></svg>www.copperfenholdings.com</div>
  </div>
  <div class="address">48 Harlow Ave, Suite 210<br>Fenwick, IA 50010</div>
</section>

</body>
</html>
```